Wine Label for new family wine label

we need a new wine label and name for our new group winemaking project. There are 10 of us in the group, plus two wine growers and two winemakers. We will be making wines on an ongoing basis but relatively small scale. The wines will be coming from the barossa valley and coonawarra. They will be high end wines - built on great dirt, some great history with the growers, and ultimately great grapes. We will be initially producing 4 wines, a shiraz, a cab, and a blend plus one high end single block shiraz based wine.

We are looking for the wine label to reflect quality, family and friendship.

```html
<!DOCTYPE html>
<html lang="en">
<head>
<meta charset="utf-8">
<title>Vellara Shiraz 2014 — Wine Label</title>
<link rel="stylesheet" href="https://fonts.googleapis.com/css2?family=Kaushan+Script&family=Open+Sans:wght@300;600&family=Roboto+Condensed:wght@300&display=swap">
<style>
  :root {
    --label-white: #ffffff;
    --label-edge: #e6e6e6;
    --plum: #722b7a;
    --ink-grey: #5f5f5f;
    --rule-grey: #6a6a6a;
  }
  html, body {
    margin: 0;
    padding: 0;
    width: 1062px;
    height: 1200px;
    overflow: hidden;
    background: var(--label-white);
  }
  .label {
    position: relative;
    width: 1062px;
    height: 1200px;
    background: var(--label-white);
  }
  .label-outline {
    position: absolute;
    inset: 0;
  }
  .brand-dot {
    position: absolute;
    left: 420px;
    top: 190px;
    width: 220px;
    height: 220px;
    border-radius: 50%;
    background: var(--plum);
  }
  .brand-name {
    position: absolute;
    left: 0;
    width: 1062px;
    top: 560px;
    margin: 0;
    text-align: center;
    font-family: "Open Sans", sans-serif;
    font-weight: 600;
    font-size: 92px;
    line-height: 1;
    color: var(--plum);
    padding-left: 20px;
    box-sizing: border-box;
  }
  .regions {
    position: absolute;
    top: 708px;
    left: 0;
    width: 1062px;
    font-family: "Kaushan Script", cursive;
    font-size: 33px;
    line-height: 1;
    color: var(--ink-grey);
  }
  .region {
    position: absolute;
    top: 0;
    white-space: nowrap;
  }
  .region-west { right: calc(1062px - 530px); }
  .region-east { left: 565px; }
  .centre-rule {
    position: absolute;
    left: 547px;
    top: 717px;
    width: 4px;
    height: 188px;
    background: var(--rule-grey);
  }
  .varietal {
    position: absolute;
    left: 0;
    width: 1062px;
    top: 900px;
    margin: 0;
    text-align: center;
    font-family: "Open Sans", sans-serif;
    font-weight: 300;
    font-size: 80px;
    line-height: 1;
    letter-spacing: 0.22em;
    color: var(--ink-grey);
    padding-left: 28px;
    box-sizing: border-box;
  }
  .detail {
    position: absolute;
    left: 0;
    width: 1062px;
    margin: 0;
    text-align: center;
    font-family: "Roboto Condensed", sans-serif;
    font-weight: 300;
    font-size: 34px;
    line-height: 1;
    color: var(--ink-grey);
    padding-left: 10px;
    box-sizing: border-box;
  }
  .vintage { top: 1002px; }
  .volume { top: 1055px; }
</style>
</head>
<body>
  <main class="label">
    <svg class="label-outline" width="1062" height="1200" viewBox="0 0 1062 1200" aria-hidden="true">
      <path d="M1 1199 V181 H358 A172 172 0 0 1 702 181 H1061 V1199 Z"
            fill="var(--label-white)" stroke="var(--label-edge)" stroke-width="2"/>
    </svg>

    <div class="brand-dot" aria-hidden="true"></div>
    <h1 class="brand-name">Vellara</h1>

    <div class="regions">
      <span class="region region-west">Barossa valley</span>
      <span class="region region-east">Coonawarra</span>
    </div>
    <div class="centre-rule" aria-hidden="true"></div>

    <h2 class="varietal">Shiraz</h2>
    <p class="detail vintage">2014</p>
    <p class="detail volume">750 ml</p>
  </main>
</body>
</html>
```